Flyer for The Quiet Bloom Gathering

I am launching my new offering in my business at an event next Sunday where I have a booth and need a flyer advertising the offering, so the flyer needs to stand out for other practitioners that will also be there on the day offering there services.
This flyer is also what I will use for marketing on social media as well as on the day of the event. See the link below to the offering
http://sarahlindqvist.com.au/quiet-bloom-gathering/

Target Market(s)

Women with body image issues - age range 25 - 65
Women with issues around food such as binge eating, emotional eating, eating disorders.

Industry/Entity Type

Health And Wellness

Font styles to use
Serif
Sans Serif
Script

Colors
f9d9e8
85cae6
cee9f5
fee18a
ffffff
eea4c8

Requirements
Must have
• Colours matching my overall website at sarahlindqvist.com.au - pinks, light blue, gold, white
• Imagery similiar to my Instagram, see below https://www.instagram.com/riverstonecarexy/
• - soft, warm, welcoming, nurturing, safe, inviting - see image on sales page for inspiration
• contact details
Should not have
• harsh dark colours or harsh lines

```html
<!DOCTYPE html>
<html lang="en">
<head>
<meta charset="utf-8">
<title>The Quiet Bloom Gathering – Flyer</title>
<link rel="stylesheet" href="https://fonts.googleapis.com/css2?family=Patrick+Hand&family=Fira+Sans+Condensed:wght@400;500;600&display=swap">
<style>
  :root{
    --stage:#c8c8c8;
    --sky:#a9cbec;
    --sky-soft:#d3e6f6;
    --blue:#29a8e0;
    --magenta:#b4318c;
    --pink:#d94fa6;
    --lilac:#c9a6dc;
    --ink:#151515;
    --white:#ffffff;
    --hand:"Patrick Hand", cursive;
    --body:"Fira Sans Condensed", sans-serif;
  }
  *{box-sizing:border-box;margin:0;padding:0}
  html,body{width:1200px;height:900px;overflow:hidden;background:var(--stage)}
  .canvas{position:relative;width:1200px;height:900px;font-family:var(--body);color:var(--ink)}
  .page{position:absolute;top:84px;width:519px;height:733px;overflow:hidden}
  .page--front{left:69px;background:linear-gradient(180deg,var(--sky) 0%,var(--sky-soft) 45%,#ecd9ea 62%)}
  .page--back{left:612px;background:var(--white)}
  .abs{position:absolute}

  .brand{position:absolute;display:flex;align-items:center;gap:12px;color:var(--blue);font-family:var(--body);font-weight:500}
  .brand__dot{flex:none;border-radius:50%;background:var(--blue)}
  .page--front .brand{left:0;width:519px;top:88px;justify-content:center;font-size:30px}
  .page--front .brand__dot{width:16px;height:16px}
  .page--back .brand{left:36px;top:62px;width:125px;font-size:21px;line-height:1.1}
  .page--back .brand__dot{width:12px;height:12px}

  .field-photo{left:0;top:420px;width:519px;height:313px;
    background:linear-gradient(180deg,rgba(214,120,190,0) 0%,rgba(214,120,190,.55) 14%,#d466b3 35%,#c2459d 70%,#a83187 100%)}
  .front-headline{left:0;width:519px;top:200px;text-align:center;font-family:var(--hand);font-size:30px;font-weight:400;line-height:39px;text-transform:uppercase}
  .front-intro{left:0;width:519px;top:294px;text-align:center;font-size:12.5px;line-height:18.2px}
  .front-question{left:0;width:519px;top:464px;text-align:center;font-size:17px;font-weight:500;line-height:25px}
  .turn-tab{left:306px;top:556px;width:213px;height:33px;background:var(--blue);clip-path:polygon(14px 0,100% 0,100% 100%,0 100%);
    color:var(--white);font-size:17px;font-weight:500;line-height:33px;padding-left:40px}
  .signature{text-align:center}
  .signature__name{font-family:var(--body);font-weight:400;letter-spacing:1px}
  .signature__tag{font-size:7px}
  .page--front .signature{left:140px;top:650px;width:240px;color:var(--white)}
  .page--front .signature__name{font-size:30px}

  .sitting-photo{left:250px;top:0;width:269px;height:733px;
    background:radial-gradient(ellipse at 60% 55%,#9c7fc9 0%,#b99ad8 35%,rgba(240,220,245,.6) 65%,rgba(255,255,255,0) 85%)}
  .mist{left:0;top:0;width:519px;height:733px;background:linear-gradient(180deg,rgba(243,195,226,.35),rgba(255,255,255,0) 35%,rgba(255,255,255,0) 85%,rgba(180,150,210,.5))}
  .back-lead{left:175px;top:45px;width:335px;font-family:var(--hand);font-size:17px;line-height:20px;text-transform:uppercase}
  .back-lead p{margin-bottom:8px}
  .section-title{color:var(--blue);font-size:18px;font-weight:500}
  .back-title{left:41px;top:190px}
  .back-body{left:41px;top:218px;width:330px;font-size:11px;line-height:15px}
  .back-body p{margin-bottom:8px}
  .offer-band{left:0;top:329px;width:363px;height:181px;background:var(--magenta);clip-path:polygon(0 0,100% 0,84% 100%,0 100%);color:var(--white)}
  .offer-band h3{position:absolute;left:41px;top:14px;font-size:11px;font-weight:600}
  .offer-list{position:absolute;left:41px;top:36px;width:275px;list-style:none;font-size:10.8px;line-height:13px}
  .offer-list li{position:relative;padding-left:22px;margin-bottom:9px}
  .offer-list svg{position:absolute;left:0;top:0}
  .price{left:41px;top:521px;width:340px;font-size:11px;line-height:14px}
  .signup{left:41px;top:578px}
  .page--back .signature{left:38px;top:620px;width:210px;color:var(--pink)}
  .page--back .signature__name{font-size:24px}
  .page--back .signature__tag{color:var(--blue)}
  .contact-box{left:275px;top:580px;width:208px;height:55px;background:var(--blue);color:var(--white);font-size:11px;padding:9px 0 0 20px}
  .contact-box div{display:flex;align-items:center;gap:8px;height:19px}
  .social{left:301px;top:644px;display:flex;gap:13px}
  .social span{width:28px;height:28px;border-radius:50%;background:var(--white);display:block}
</style>
</head>
<body>
<main class="canvas">

  <section class="page page--front">
    <div class="abs field-photo" role="img" aria-label="Photo of a woman with arms open wide in a field of flowers, tinted pink"></div>
    <div class="brand"><span class="brand__dot"></span>The Quiet Bloom Gathering</div>
    <h1 class="abs front-headline">It’s time to make a commitment…<br>It’s time for you, to show up for you…</h1>
    <p class="abs front-intro">
      It’s time to make a commitment….<br>
      It’s time for YOU, to SHOW UP for YOU…..<br>
      It’s time to truly let go…….and finally heal, and find the peace that you so long for…<br>
      You deserve to feel the freedom that comes with truly loving and accepting your body.<br>
      You deserve the freedom that comes with experiencing a deeper trusting<br>
      connection with your body, where you feel safe, at home.<br>
      Can you even imagine a whole day that you didn’t hate your body,<br>
      you didn’t fight with food, and you felt peaceful and at home with your body?
    </p>
    <p class="abs front-question">Can you love the part of you, that hates your body?<br>You can’t heal something you hate.</p>
    <div class="abs turn-tab">TURN FOR DETAILS &gt;</div>
    <div class="abs signature">
      <div class="signature__name">Sarah Lindqvist</div>
      <div class="signature__tag">Come Home to Your Body, Make Peace with Your Plate</div>
    </div>
  </section>

  <section class="page page--back">
    <div class="abs sitting-photo" role="img" aria-label="Photo of a woman seated cross-legged gazing at a soft misty sky, tinted lilac"></div>
    <div class="abs mist"></div>
    <div class="brand"><span class="brand__dot"></span><span>The Quiet Bloom Gathering</span></div>
    <div class="abs back-lead">
      <p>It’s time to show up for you, consistently, every week, and do the work, once and for all.</p>
      <p>No more games, no more half in on you…</p>
      <p>You deserve better than a life contained in the mental prison of body hatred.</p>
    </div>
    <h2 class="abs section-title back-title">Are you truly ready to make the commitment?</h2>
    <div class="abs back-body">
      <p>How would it feel to be able to say, <b>“I am free to love and accept my body”</b>, and <b>“I am free, connected and at peace to my body”</b>?</p>
      <p>I am inviting 10 women only into this six-week healing experience, as I personally know, that when we share our stories, it opens our hearts for other people to share their stories. It gives us the sense we are not alone in our journey’s.</p>
    </div>
    <div class="abs offer-band">
      <h3>The women that come on this six-week journey will receive;</h3>
      <ul class="offer-list">
        <li><svg width="13" height="12" viewBox="0 0 13 12"><path d="M1 6.5l3.5 4L12 1" fill="none" stroke="#fff" stroke-width="1.8"/></svg>One 90mins one on one coaching session with me (which for the women that have attended the Friday circle previously, can be done before this healing circle begins);</li>
        <li><svg width="13" height="12" viewBox="0 0 13 12"><path d="M1 6.5l3.5 4L12 1" fill="none" stroke="#fff" stroke-width="1.8"/></svg>Private Online Group to continue support outside of the circle</li>
        <li><svg width="13" height="12" viewBox="0 0 13 12"><path d="M1 6.5l3.5 4L12 1" fill="none" stroke="#fff" stroke-width="1.8"/></svg>Homework outside of circle to support your healing</li>
        <li><svg width="13" height="12" viewBox="0 0 13 12"><path d="M1 6.5l3.5 4L12 1" fill="none" stroke="#fff" stroke-width="1.8"/></svg>Journal and other small gifts weekly</li>
      </ul>
    </div>
    <p class="abs price">The financial investment in YOU, is $XX for the six weeks. For the women that have attended the Friday night, Gentle Bloom Sister Circle, you will receive a discount of $XX, taking the price to $XX.</p>
    <h2 class="abs section-title signup">Are you ready? Sign Up Now!</h2>
    <div class="abs signature">
      <div class="signature__name">Sarah Lindqvist</div>
      <div class="signature__tag">Come Home to Your Body, Make Peace with Your Plate</div>
    </div>
    <div class="abs contact-box">
      <div><svg width="12" height="12" viewBox="0 0 12 12"><path d="M2.5 1l2 2.5-1 1.2c.7 1.5 1.8 2.6 3.3 3.3l1.2-1 2.5 2-1 1.8C5 10.5 1.5 7 .8 2z" fill="#fff"/></svg>0412 555 019</div>
      <div><svg width="13" height="10" viewBox="0 0 13 10"><rect x=".5" y=".5" width="12" height="9" fill="#fff"/><path d="M.5 .5l6 5 6-5" fill="none" stroke="#29a8e0" stroke-width="1"/></svg>sarah@sarahlindqvist.com.au</div>
    </div>
    <div class="abs social" aria-label="Social media links">
      <span></span><span></span><span></span><span></span>
    </div>
  </section>

</main>
</body>
</html>
```